Vela Korth

Graphic design for web pages depicting an environmental solution to human waste streams of plastic, tyres and bio mass, converting waste to energy. Technology used is a pyrolysis plant deconstructing 20tonnes per day of waste. Also touch up of logo

```html
<!DOCTYPE html>
<html lang="en">
<head>
<meta charset="utf-8">
<title>Vela Korth — Pyrolysis Plant</title>
<link href="https://fonts.googleapis.com/css2?family=Poppins:wght@300;400;500;600&display=swap" rel="stylesheet">
<style>
:root{
  --green:#3dbb6a;
  --green-text:#2ea552;
  --ink:#111111;
  --body:#444444;
  --muted:#888888;
  --panel:#f2f2f2;
  --footer:#262626;
  --white:#ffffff;
}
*{margin:0;padding:0;box-sizing:border-box}
html,body{width:678px;height:1200px;overflow:hidden;background:var(--white)}
body{font-family:'Poppins',sans-serif;color:var(--ink);position:relative}
.abs{position:absolute}

/* header */
.site-header{position:absolute;left:0;top:0;width:678px;height:54.5px;background:var(--white)}
.brand{position:absolute;left:132px;top:19px;display:flex;align-items:center;gap:4px;font-weight:600;font-size:11px;color:var(--ink);white-space:nowrap}
.brand-mark{width:9px;height:9px;background:var(--green)}
.main-nav{position:absolute;top:25px;font-size:5.4px;font-weight:500;letter-spacing:.1px}
.main-nav span{position:absolute;white-space:nowrap}
.main-nav .active{color:var(--green-text)}

/* hero */
.hero{position:absolute;left:0;top:54.5px;width:678px;height:205px;background:linear-gradient(90deg,#2c80b4 0%,#4a9c86 40%,#6cb546 70%,#84bd34 100%)}
.hero-title{position:absolute;left:0;width:678px;top:64px;text-align:center;color:var(--white);font-weight:600;font-size:15px}
.hero-text{position:absolute;left:190px;width:298px;top:87px;text-align:center;color:var(--white);font-size:7.4px;line-height:10.6px}
.btn{position:absolute;background:var(--green);color:var(--white);font-weight:600;font-size:6.2px;letter-spacing:.5px;display:flex;align-items:center;justify-content:center}
.hero-arrow{position:absolute;width:26px;height:26px;border-radius:50%;background:var(--green);top:90px}
.dot{position:absolute;top:181px;width:5px;height:5px;border-radius:50%;border:1px solid var(--white)}
.dot.current{background:var(--green)}

/* section headings */
.kicker-bar{position:absolute;left:132px;width:3.5px;background:var(--green)}
.kicker{position:absolute;left:143px;font-size:6px;font-weight:500;color:var(--green-text)}
.section-title{position:absolute;left:143px;font-size:14px;font-weight:600;white-space:nowrap}

.about-text{position:absolute;left:132px;top:320px;width:190px;font-size:4.9px;line-height:9.2px;color:var(--body)}
.video-frame{position:absolute;left:344.4px;top:290.8px;width:200.8px;height:135.6px;background:linear-gradient(180deg,#1f5fa0 0%,#3f86c4 55%,#8fa2b3 100%)}

.services{position:absolute;left:0;top:455.3px;width:678px;height:260.5px;background:var(--panel)}
.card{position:absolute;background:var(--white);width:130.5px}
.card-img{position:absolute;left:0;top:0;width:100%}
.card-title{position:absolute;left:8.8px;font-size:8px;font-weight:500;white-space:nowrap}
.card-text{position:absolute;left:8.8px;width:116px;font-size:5px;line-height:8.5px;color:var(--body)}
.read-more{position:absolute;left:8.8px;font-size:4.8px;font-weight:600;color:var(--green-text);text-decoration:underline}

.news-card{border:0.5px solid #e6e6e6}
.news-card .card-img{border-bottom:1.4px solid var(--green)}
.news-title{position:absolute;left:10.7px;width:115px;font-size:6.5px;line-height:9.3px;font-weight:500}
.news-text{position:absolute;left:10.7px;width:115px;font-size:5.1px;line-height:8.4px;color:var(--body)}
.news-meta{position:absolute;left:10.7px;font-size:5.2px;font-weight:300;color:var(--muted);display:flex;gap:5px;white-space:nowrap}

/* footer */
.site-footer{position:absolute;left:0;top:1035.5px;width:678px;height:164.5px;background:var(--footer);color:var(--white)}
.footer-brand{position:absolute;left:132px;top:29px;display:flex;align-items:center;gap:4px;font-weight:600;font-size:11px;white-space:nowrap}
.footer-about{position:absolute;left:132px;top:62px;width:135px;font-size:5px;line-height:8.4px}
.social{position:absolute;top:96px;width:14.5px;height:14.5px;border:0.6px solid #cfcfcf}
.footer-head{position:absolute;top:25px;font-size:5.6px;font-weight:600;white-space:nowrap}
.footer-head::after{content:"";position:absolute;left:0;top:11px;width:15px;height:0.9px;background:var(--green)}
.link-list{position:absolute;list-style:none;font-size:5.1px}
.link-list li{position:absolute;white-space:nowrap;padding-left:7px}
.link-list li::before{content:"›";position:absolute;left:0;top:-0.5px}
.contact-line{position:absolute;left:450.6px;font-size:5.1px;line-height:8.2px;width:100px}
.contact-icon{position:absolute;left:440.5px}
.footer-rule{position:absolute;left:132px;top:128.5px;width:413px;height:0.5px;background:#444}
.copyright{position:absolute;left:0;width:678px;top:144px;text-align:center;font-size:5.1px}
.copyright em{font-style:normal;color:var(--green)}
</style>
</head>
<body>

<header class="site-header">
  <div class="brand"><span class="brand-mark"></span>Vela Korth</div>
  <nav class="main-nav">
    <span class="active" style="left:269px">HOME</span>
    <span style="left:304px">ABOUT</span>
    <span style="left:340px">TECHNOLOGY</span>
    <span style="left:396px">SOLUTIONS</span>
    <span style="left:445px">VIDEOS</span>
    <span style="left:483px">NEWS</span>
    <span style="left:517px">CONTACT</span>
  </nav>
</header>

<section class="hero" role="img" aria-label="Two engineers in hard hats shaking hands in front of a pyrolysis plant, tinted blue to green">
  <div class="hero-arrow" style="left:61px">
    <svg width="26" height="26" viewBox="0 0 26 26"><path d="M14.5 8.5 10 13l4.5 4.5" fill="none" stroke="#fff" stroke-width="1.6"/></svg>
  </div>
  <div class="hero-arrow" style="left:589px">
    <svg width="26" height="26" viewBox="0 0 26 26"><path d="M11.5 8.5 16 13l-4.5 4.5" fill="none" stroke="#fff" stroke-width="1.6"/></svg>
  </div>
  <h1 class="hero-title">PYROLYSIS PLANT</h1>
  <p class="hero-text">Environmental solution to human waste streams of plastic, tyres and bio mass, converting waste to energy. Technology used is a pyrolysis plant deconstructing 20 tonnes per day of waste.</p>
  <div class="btn" style="left:304px;top:129px;width:70px;height:22px">LEARN MORE</div>
  <span class="dot current" style="left:328px"></span>
  <span class="dot" style="left:336.5px"></span>
  <span class="dot" style="left:345px"></span>
</section>

<!-- about -->
<div class="kicker-bar" style="top:292px;height:20px"></div>
<div class="kicker" style="top:291.5px">WHAT WE DO</div>
<h2 class="section-title" style="top:297px">VELA KORTH</h2>
<p class="about-text">Lorem ipsum dolor sit amet, consectetur adipiscing elit. Nunc fermentum pretium sem, ut accumsan justo dapibus quis. Aliquam in neque placerat, suscipit massa ac, pharetra libero. Pellentesque at magna arcu. Etiam et congue massa. Nullam ex leo, commodo et congue non, commodo non erat. Morbi auctor lectus erat, vel tincidunt nisi fermentum id. Curabitur et ultrices nisi. Aenean tristique sapien quis magna molestie fermentum. Maecenas id mattis massa, quis ornare ipsum. In rhoncus ex est.</p>
<div class="btn" style="left:132px;top:394.7px;width:71px;height:22px">LEARN MORE</div>
<div class="video-frame" role="img" aria-label="Video still of a pyrolysis plant tower at dusk">
  <svg class="abs" style="left:84.8px;top:52.6px" width="31" height="31" viewBox="0 0 31 31">
    <circle cx="15.5" cy="15.5" r="14.5" fill="none" stroke="#fff" stroke-width="1.6"/>
    <path d="M12.5 9.5v12l9.5-6z" fill="#fff"/>
  </svg>
</div>

<!-- services -->
<section class="services">
  <div class="kicker-bar" style="top:26.5px;height:20px"></div>
  <div class="kicker" style="top:26px">SERVICES</div>
  <h2 class="section-title" style="top:32px">PYROLYSIS &amp; RECYCLING EQUIPMENT</h2>

  <article class="card" style="left:132.3px;top:69.7px;height:162.8px">
    <div class="card-img" style="height:90px;background:linear-gradient(180deg,#9fb8cc,#8c8c88 60%,#7a776e)" role="img" aria-label="Two tyre pyrolysis reactors on site"></div>
    <h3 class="card-title" style="top:99.5px">Tyre Recycling Plant</h3>
    <p class="card-text" style="top:115.5px">Donec nisi eros, blandit sit amet semper rhoncus, convallis a ipsum. Lorem ipsum dolor sit amet, consectetur adipiscing elit.</p>
    <a class="read-more" style="top:144.5px">READ MORE</a>
  </article>
  <article class="card" style="left:273.5px;top:69.7px;height:162.8px">
    <div class="card-img" style="height:90px;background:linear-gradient(180deg,#a9bfd2,#8d8a80 55%,#6d665a)" role="img" aria-label="Plastic recycling plant with reactor and pipework"></div>
    <h3 class="card-title" style="top:99.5px">Plastic Recycling Plant</h3>
    <p class="card-text" style="top:115.5px">Donec nisi eros, blandit sit amet semper rhoncus, convallis a ipsum. Lorem ipsum dolor sit amet, consectetur adipiscing elit.</p>
    <a class="read-more" style="top:144.5px">READ MORE</a>
  </article>
  <article class="card" style="left:415.2px;top:69.7px;height:162.8px">
    <div class="card-img" style="height:90px;background:linear-gradient(135deg,#6e6a66,#4f6f8f 45%,#9b6e5e 80%,#5e5a55)" role="img" aria-label="Collage of plant accessories and machinery parts"></div>
    <h3 class="card-title" style="top:99.5px">Accessories</h3>
    <p class="card-text" style="top:115.5px">Donec nisi eros, blandit sit amet semper rhoncus, convallis a ipsum. Lorem ipsum dolor sit amet, consectetur adipiscing elit.</p>
    <a class="read-more" style="top:144.5px">READ MORE</a>
  </article>
</section>

<!-- news -->
<div class="kicker-bar" style="top:742.8px;height:20px"></div>
<div class="kicker" style="top:742.5px">NEWS</div>
<h2 class="section-title" style="top:748px">LATEST NEWS</h2>

<article class="card news-card" style="left:132.3px;top:782.4px;height:175.2px">
  <div class="card-img" style="height:86.7px;background:linear-gradient(180deg,#d8dcdf,#a9afb3 60%,#8f9498)" role="img" aria-label="Industrial filter units against a concrete wall"></div>
  <h3 class="news-title" style="top:97px">liquam blandit ultricies pharetra. Nam dignissim suscipit dolor</h3>
  <p class="news-text" style="top:122.5px">Etiam ullamcorper orci eget aliquet sagittis. Proin sed nulla vel mi tincidunt viverra vel eget ex.</p>
  <div class="news-meta" style="top:153px"><span>◷ Nov 26</span><span>✉ 2 Comments</span></div>
</article>
<article class="card news-card" style="left:273.5px;top:782.4px;height:175.2px">
  <div class="card-img" style="height:86.7px;background:linear-gradient(180deg,#c9d9c4,#a4bd93 45%,#5f9a3a 75%,#4b8230)" role="img" aria-label="Wind turbines over a green field"></div>
  <h3 class="news-title" style="top:97px">liquam blandit ultricies pharetra. Nam dignissim suscipit dolor</h3>
  <p class="news-text" style="top:122.5px">Etiam ullamcorper orci eget aliquet sagittis. Proin sed nulla vel mi tincidunt viverra vel eget ex.</p>
  <div class="news-meta" style="top:153px"><span>◷ Nov 26</span><span>✉ 2 Comments</span></div>
</article>
<article class="card news-card" style="left:415.2px;top:782.4px;height:175.2px">
  <div class="card-img" style="height:86.7px;background:linear-gradient(135deg,#6f8f4e,#3fa25a 50%,#7aa35a)" role="img" aria-label="Two children in recycling shirts giving thumbs up"></div>
  <h3 class="news-title" style="top:97px">liquam blandit ultricies pharetra. Nam dignissim suscipit dolor</h3>
  <p class="news-text" style="top:122.5px">Etiam ullamcorper orci eget aliquet sagittis. Proin sed nulla vel mi tincidunt viverra vel eget ex.</p>
  <div class="news-meta" style="top:153px"><span>◷ Nov 26</span><span>✉ 2 Comments</span></div>
</article>

<div class="btn" style="left:304px;top:981.4px;width:70px;height:21.4px">MORE NEWS</div>

<footer class="site-footer">
  <div class="footer-brand"><span class="brand-mark"></span>Vela Korth</div>
  <p class="footer-about">Lorem ipsum dolor sit amet, consectetur adipiscing elit. Nunc fermentum pretium sem, ut accumsan justo dapibus quis.</p>
  <span class="social" style="left:132.3px"></span>
  <span class="social" style="left:150.5px"></span>
  <span class="social" style="left:168.7px"></span>
  <span class="social" style="left:186.9px"></span>

  <h4 class="footer-head" style="left:282px">QUICK LINKS</h4>
  <ul class="link-list" style="left:282px;top:0">
    <li style="top:48px">Home</li>
    <li style="top:60px">Technology</li>
    <li style="top:72px">Solutions</li>
    <li style="top:84px">videos</li>
    <li style="top:96px">News</li>
  </ul>

  <h4 class="footer-head" style="left:345.3px">USEFUL LINKS</h4>
  <ul class="link-list" style="left:345.3px;top:0">
    <li style="top:48px">About</li>
    <li style="top:60px">Terms of Service</li>
    <li style="top:72px">Privacy Policy</li>
    <li style="top:84px">Frequently Asked Questions</li>
    <li style="top:96px">Contact</li>
  </ul>

  <h4 class="footer-head" style="left:440.8px">CONTACT US</h4>
  <svg class="contact-icon" style="top:49px" width="5" height="7" viewBox="0 0 10 14"><path d="M5 0a5 5 0 0 0-5 5c0 4 5 9 5 9s5-5 5-9a5 5 0 0 0-5-5zm0 7a2 2 0 1 1 0-4 2 2 0 0 1 0 4z" fill="#3dbb6a"/></svg>
  <p class="contact-line" style="top:47px">48 Fernhollow Rd, Unit 12, Marlow Bay, QLD 4870, Australia</p>
  <svg class="contact-icon" style="top:69.5px" width="5.5" height="5.5" viewBox="0 0 12 12"><path d="M2.5 0 4.5 2.8 3.3 4.3a7 7 0 0 0 4.4 4.4l1.5-1.2L12 9.5 10.6 12C5 12 0 7 0 1.4z" fill="#3dbb6a"/></svg>
  <p class="contact-line" style="top:68px">(07) 5550 2194</p>
  <svg class="contact-icon" style="top:83px" width="6" height="4.5" viewBox="0 0 12 9"><rect width="12" height="9" fill="#3dbb6a"/><path d="M0 0l6 5 6-5" fill="none" stroke="#262626" stroke-width="1"/></svg>
  <p class="contact-line" style="top:81px">hello@velakorth.example</p>

  <div class="footer-rule"></div>
  <p class="copyright">Copyright © 2019 <em>VELA KORTH</em>. All Rights Reserved.</p>
</footer>

</body>
</html>
```